Updated web design for software design firm supporting entrepreneurs

Looking for a more modern looking, mobile friendly website design for our company, Plans4Buildables. P4B is a software development firm who supports people who have ideas for software and want to make them a reality. It also provides some maintenance work on existing websites as well as mobile apps. Please see our current website, www.plans4buildables-example.com, for more information on our business.

Old logo files included for reference. However, we are hoping to incorporate a new logo.

Like a blue'ish theme, but open to ideas.

Industry/Entity Type

Software

Logo Text

P4B and/or Plans4Buildables

Number of Pages Required

2 page

Font styles to use
Serif
Sans Serif

Colors
33a6d7
0255a3

Requirements
Must have
• Looking for 2 pages designed: 1 landing page and 1 type of secondary content page
• Please prepare menu for about 7 pages
Nice to have
• This will be implemented as a WordPress theme.
• Could include post-it note, white board, napkins, etc.

```html
<!DOCTYPE html>
<html lang="en">
<head>
<meta charset="utf-8">
<title>About Us – Plans4Buildables</title>
<link href="https://fonts.googleapis.com/css2?family=Montserrat:wght@600;700&family=Open+Sans:wght@400;600&family=Lato:wght@400;700&display=swap" rel="stylesheet">
<style>
:root{
  --brand-blue:#0255a3;
  --accent-blue:#33a6d7;
  --ink:#2b2b2b;
  --text:#3c3c3c;
  --dark-band:#333333;
  --footer-bg:#f1f1f1;
  --white:#ffffff;
}
*{margin:0;padding:0;box-sizing:border-box}
html,body{width:689px;height:1200px;overflow:hidden}
body{position:relative;background:var(--white);font-family:"Lato",sans-serif;color:var(--text)}
.abs{position:absolute}

/* header */
.site-header{left:0;top:0;width:689px;height:69px;background:var(--white)}
.brand{left:56px;top:14px;display:flex;align-items:center;gap:6px;font-family:"Montserrat",sans-serif;font-weight:700;font-size:20px;color:var(--brand-blue)}
.brand-dot{width:12px;height:12px;border-radius:50%;background:var(--brand-blue)}
.top-contact{right:57px;top:10px;display:flex;gap:10px;align-items:center;font-family:"Open Sans",sans-serif;font-size:9.5px;font-weight:600}
.top-contact span{display:flex;align-items:center;gap:5px}
.top-contact .mail{color:var(--accent-blue)}
.top-contact .phone{color:var(--brand-blue)}
.icon-badge{width:19px;height:19px;border-radius:50%;display:flex;align-items:center;justify-content:center}
.main-nav{right:57px;top:44px;display:flex;gap:15px;font-family:"Open Sans",sans-serif;font-size:8px;font-weight:600;color:#333;letter-spacing:.1px}

/* hero */
.hero{left:0;top:69px;width:689px;height:136px;background:linear-gradient(100deg,#8fa8b4 0%,#b9cdd4 45%,#c9d6c8 70%,#9fb3bb 100%)}
.hero-title{left:56px;top:124px;font-family:"Montserrat",sans-serif;font-weight:700;font-size:25px;color:var(--white)}

/* about */
.section-title{font-family:"Montserrat",sans-serif;font-weight:600;color:var(--brand-blue)}
.about-title{left:56px;top:249px;font-size:14px}
.about-rule{left:56px;top:272px;width:98px;height:1px;background:var(--brand-blue)}
.about-copy{left:56px;top:286px;width:318px;font-size:7.4px;line-height:12.8px;text-align:justify}
.about-copy p+p{margin-top:6px}
.btn{left:56px;top:419px;width:73px;height:26px;background:var(--accent-blue);color:var(--white);border-radius:3px;font-family:"Open Sans",sans-serif;font-size:8px;font-weight:600;display:flex;align-items:center;justify-content:center}
.device-visual{left:418px;top:252px;width:214px;height:192px;background:linear-gradient(160deg,#e8ebef,#c9ced6);border-radius:6px}

/* who needs us */
.audience-photo{left:0;top:488px;width:344px;height:246px;background:linear-gradient(170deg,#d9d9d9 0%,#b9b3ad 55%,#5b4c44 100%)}
.play-btn{left:154px;top:594px}
.audience-panel{left:344px;top:488px;width:345px;height:246px;background:var(--dark-band);color:var(--white)}
.panel-title{left:361px;top:512px;font-family:"Montserrat",sans-serif;font-weight:600;font-size:14px;color:var(--white)}
.panel-copy{left:363px;top:540px;width:270px;font-size:7.4px;line-height:12.8px;color:#eee}
.persona{font-family:"Montserrat",sans-serif;font-weight:700;font-size:10px;color:var(--accent-blue);margin-top:16px;margin-bottom:5px}

/* who we are */
.who-title{left:0;top:776px;width:689px;text-align:center;font-size:14px}
.who-rule{left:317px;top:802px;width:54px;height:1px;background:var(--brand-blue)}
.who-copy{left:86px;top:823px;width:517px;text-align:center;font-size:7.4px;line-height:13.6px}
.who-copy p+p{margin-top:9px}
.who-copy .hl{color:var(--accent-blue)}
.who-copy .cta{color:var(--accent-blue);font-weight:700;font-size:8.5px}

/* footer */
.site-footer{left:0;top:980px;width:689px;height:220px;background:var(--footer-bg)}
.footer-brand{left:0;top:1022px;width:689px;display:flex;justify-content:center;align-items:center;gap:6px;font-family:"Montserrat",sans-serif;font-weight:700;font-size:20px;color:var(--brand-blue)}
.footer-contact{left:0;top:1077px;width:689px;display:flex;justify-content:center;gap:12px;font-size:11.5px;color:#333}
.footer-contact span{display:flex;align-items:center;gap:6px}
.ring{width:19px;height:19px;border:1.2px solid #333;border-radius:50%;display:flex;align-items:center;justify-content:center}
.footer-nav{left:0;top:1122px;width:689px;display:flex;justify-content:center;gap:18px;font-family:"Open Sans",sans-serif;font-size:8.5px;font-weight:600;color:#222}
.footer-rule{left:56px;top:1155px;width:576px;height:1px;background:#333}
.copyright{left:56px;top:1171px;font-size:7.6px;color:#222}
.social{left:502px;top:1166px;display:flex;gap:6px}
.social span{width:21px;height:21px;border:1.2px solid #333;border-radius:50%}
</style>
</head>
<body>

<header class="abs site-header">
  <div class="abs brand"><span class="brand-dot"></span>P4B</div>
  <div class="abs top-contact">
    <span class="mail"><span class="icon-badge" style="background:var(--accent-blue)"><svg width="10" height="8" viewBox="0 0 10 8"><rect x=".6" y=".6" width="8.8" height="6.8" rx="1" fill="none" stroke="#fff" stroke-width="1"/><path d="M1 1l4 3.2L9 1" fill="none" stroke="#fff" stroke-width="1"/></svg></span>hello@plans4buildables-example.com</span>
    <span class="phone"><span class="icon-badge" style="background:var(--brand-blue)"><svg width="9" height="9" viewBox="0 0 10 10"><path d="M2 .8l1.8 2-1 1.2a6 6 0 003.2 3.2l1.2-1 2 1.8-1 1.5C5 9.5.5 5 .5 1.8z" fill="#fff"/></svg></span>(555) 014-2387</span>
  </div>
  <nav class="abs main-nav">
    <span>HOME</span><span>WHO WE ARE</span><span>HOW IT WORKS</span><span>WHO NEEDS US</span><span>ODD JOBS</span><span>PORTFOLIO</span><span>CONTACT US</span>
  </nav>
</header>

<section>
  <div class="abs hero" role="img" aria-label="Photo of two men sketching a light bulb idea on a glass board"></div>
  <h1 class="abs hero-title">ABOUT US</h1>
</section>

<section>
  <h2 class="abs section-title about-title">About Plans4Buildables</h2>
  <div class="abs about-rule"></div>
  <div class="abs about-copy">
    <p>Plans4Buildables can help anyone turn their software idea into reality. We understand that you don’t have to be a big company to have big ideas, but turning those ideas into functional software can be time consuming, expensive and seem out of reach. Plans4Buildables specializes in helping small businesses and individuals take their idea from the back of a napkin to the desktop. We’ve worked with numerous entrepreneurs and companies wanting to update their current software, whether it is making small bug fixes.</p>
    <p>As a small business ourselves, we understand the need to be flexible, efficient and cost-conscious. We’ll take your idea from a vision in your head to a fully working system. Already have software and need to make improvements? We can help there, too.</p>
  </div>
  <div class="abs btn">Read More</div>
  <div class="abs device-visual" role="img" aria-label="Desktop monitor, tablet and phone showing the company website"></div>
</section>

<section>
  <div class="abs audience-photo" role="img" aria-label="Photo of a presenter speaking to a seated audience"></div>
  <svg class="abs play-btn" width="38" height="38" viewBox="0 0 38 38"><circle cx="19" cy="19" r="17" fill="none" stroke="#fff" stroke-width="2"/><path d="M15 11l12 8-12 8z" fill="#fff"/></svg>
  <div class="abs audience-panel"></div>
  <h2 class="abs panel-title">Who Needs Us</h2>
  <div class="abs panel-copy">
    <p>Plans4Buildables is the answer for a wide range of software development needs. Below are sample fictional projects. Any resemblance to actual ideas is coincidental.</p>
    <h3 class="persona">ENTREPRENEUR</h3>
    <p>Marco has the next big idea for a smartphone app. He’s a marketing whiz and knows that he could make millions.</p>
    <h3 class="persona">SMALL BUSINESS</h3>
    <p>There are only 24 hours in a day. Plans4Buildables can work with Lena to identify specific modules of software that need to be written.</p>
  </div>
</section>

<section>
  <h2 class="abs section-title who-title">Who We Are</h2>
  <div class="abs who-rule"></div>
  <div class="abs who-copy">
    <p><span class="hl">Plans4Buildables</span> can help anyone turn their software idea into reality. We understand that you don’t have to be a big company to have big ideas, but turning those ideas into functional software can be time consuming, expensive and seem out of reach. Plans4Buildables specializes in helping small businesses and individuals take their idea from the back of a napkin to the desktop.</p>
    <p>As a small business ourselves, we understand the need to be flexible, efficient and cost-conscious. We’ll take your idea from a vision in your head to a fully working system. Already have software and need to make improvements? We can help there, too. We’ve worked with numerous entrepreneurs and companies wanting to update their current software, whether it is making small bug fixes or adding new functionality.</p>
    <p>To set up a free consultation with Plans4Buildables, please <span class="cta">contact us.</span></p>
  </div>
</section>

<footer>
  <div class="abs site-footer"></div>
  <div class="abs footer-brand"><span class="brand-dot"></span>P4B</div>
  <div class="abs footer-contact">
    <span><span class="ring"><svg width="10" height="8" viewBox="0 0 10 8"><rect x=".6" y=".6" width="8.8" height="6.8" rx="1" fill="none" stroke="#333" stroke-width="1"/><path d="M1 1l4 3.2L9 1" fill="none" stroke="#333" stroke-width="1"/></svg></span>hello@plans4buildables-example.com</span>
    <span><span class="ring"><svg width="9" height="9" viewBox="0 0 10 10"><path d="M2 .8l1.8 2-1 1.2a6 6 0 003.2 3.2l1.2-1 2 1.8-1 1.5C5 9.5.5 5 .5 1.8z" fill="none" stroke="#333" stroke-width="1"/></svg></span>(555) 014-2387</span>
  </div>
  <nav class="abs footer-nav">
    <span>HOME</span><span>|</span><span>WHO WE ARE</span><span>|</span><span>HOW IT WORKS</span><span>|</span><span>WHO NEEDS US</span><span>|</span><span>ODD JOBS</span><span>|</span><span>CONTACT</span>
  </nav>
  <div class="abs footer-rule"></div>
  <p class="abs copyright">Copyright © 2017 Plans4Buildables. All Right Reserved</p>
  <div class="abs social" aria-label="Social media links"><span></span><span></span><span></span><span></span><span></span></div>
</footer>

</body>
</html>
```